EXTENDED Store hours to serve your healthcare needs

I'M LOOKING FOR A NICE FLYER THAT SHOWS THE FOLLOWING INFORMATION:

Logo
address
tel phone and fax
email address

Extending our hours to meet the growing healthcare needs of our community. Fast delivery service!

Monday - Thursday 10am-midnight
Friday 10am-4pm
Saturday - Motzei Shabbos till midnight
Sunday 10am-7pm

Target Market(s)

Community

Industry/Entity Type

Pharmacy

Requirements
Must have
• Extended hours
• personal care
• expert advice
• superior service
Nice to have
• Looking for no people pictures
• Eye popping design
• Classic modern clean design
Should not have
• store description is services
• And should not say Fiirst to open and last to close

```html
<!DOCTYPE html>
<html lang="en">
<head>
<meta charset="utf-8">
<title>Kessler Pharmacy – Extended Hours</title>
<link href="https://fonts.googleapis.com/css2?family=Roboto:ital,wght@0,300;0,400;0,700;0,900;1,700;1,900&family=Roboto+Condensed:wght@400&display=swap" rel="stylesheet">
<style>
  :root{
    --blue:#2a55a8;
    --red:#c4202a;
    --ink:#111111;
    --yellow:#f2f51c;
    --green:#1b8a1b;
    --paper:#ffffff;
    --board:#e8e9ec;
    --row-a:#ffffff;
    --row-b:#e2e3e6;
  }
  *{margin:0;padding:0;box-sizing:border-box}
  html,body{width:846px;height:1200px;overflow:hidden;background:var(--paper)}
  body{font-family:"Roboto",Arial,sans-serif;color:var(--ink)}
  .flyer{position:relative;width:846px;height:1200px;background:var(--board);overflow:hidden}

  .hero{position:absolute;left:0;top:0;width:846px;height:490px;
    background:linear-gradient(180deg,#ffffff 0%,#f1f3f6 45%,#f7f8fa 100%)}
  .hero-photo{position:absolute;left:0;top:150px;width:846px;height:340px;
    background:radial-gradient(ellipse at 55% 30%,rgba(180,195,215,.35),rgba(255,255,255,0) 70%)}

  .brand{position:absolute;left:140px;top:70px;display:flex;align-items:center;gap:18px}
  .brand-mark{width:46px;height:46px;background:var(--blue)}
  .brand-name{font-family:"Roboto",Arial,sans-serif;font-weight:700;font-size:64px;
    color:var(--red);letter-spacing:1px;line-height:1}
  .brand-sub{position:absolute;left:454px;top:158px;font-weight:400;font-size:34px;
    letter-spacing:7px;color:var(--blue)}

  .headline{position:absolute;left:0;top:0}
  .headline text{font-family:"Roboto",Arial,sans-serif}
  .b{font-weight:900}.l{font-weight:300}
  .c-blue{fill:var(--blue)}.c-red{fill:var(--red)}.c-ink{fill:var(--ink)}

  .banner{position:absolute;left:0;top:508px}
  .banner text{font-family:"Roboto",Arial,sans-serif;font-style:italic}

  .features{position:absolute;left:0;top:585px;width:846px;display:flex}
  .feature{position:absolute;width:200px;text-align:center;transform:translateX(-50%)}
  .feature svg{display:block;margin:0 auto;width:64px;height:64px}
  .feature h3{margin-top:30px;font-weight:700;font-size:24px;line-height:24px;letter-spacing:.3px}
  .feature p{margin-top:5px;font-size:14px;line-height:15px;font-weight:400;color:#222}

  .hours{position:absolute;left:110px;top:822px;width:620px;border-collapse:collapse;
    border-radius:12px;overflow:hidden;font-size:17px}
  .hours th{background:var(--blue);color:#fff;font-weight:700;font-size:21px;height:32px}
  .hours td{height:34.3px;border-right:1px solid #c8c9cc;
    background:linear-gradient(180deg,var(--row-a),var(--row-b))}
  .hours td:last-child,.hours th:last-child{border-right:none}
  .hours th{border-right:1px solid #4d6fb5}
  .hours .day{width:182px;text-align:right;padding-right:58px}
  .hours .time{width:264px;text-align:center;font-weight:300}
  .hours .status{text-align:center;color:var(--green);font-weight:700;font-style:italic;padding-right:30px}
  .hours tfoot td{background:var(--blue);height:24px;border-right:1px solid #4d6fb5}

  .footer{position:absolute;left:0;top:1159px;width:846px;height:41px;display:flex;
    font-family:"Roboto Condensed","Roboto",sans-serif;color:#fff;font-size:21px;letter-spacing:2.6px}
  .footer .address{width:440px;background:var(--red);padding:8px 0 0 30px}
  .footer .email{flex:1;background:var(--blue);padding:8px 0 0 25px}
</style>
</head>
<body>
<div class="flyer">
  <section class="hero">
    <div class="hero-photo" role="img" aria-label="Soft, blurred photo of pills and medicine packs on a pharmacy counter"></div>
    <div class="brand">
      <span class="brand-mark"></span>
      <span class="brand-name">Kessler</span>
    </div>
    <div class="brand-sub">PHARMACY</div>

    <svg class="headline" width="846" height="490" viewBox="0 0 846 490">
      <text x="45" y="280" font-size="72" textLength="755" lengthAdjust="spacingAndGlyphs">
        <tspan class="b c-blue">EXTENDING</tspan><tspan class="l c-ink"> OUR </tspan><tspan class="b c-red">HOURS</tspan></text>
      <text x="78" y="344" font-size="72" textLength="682" lengthAdjust="spacingAndGlyphs">
        <tspan class="l c-ink">TO </tspan><tspan class="b c-ink">MEET</tspan><tspan class="l c-ink"> THE </tspan><tspan class="b c-ink">GROWING</tspan></text>
      <text x="34" y="416" font-size="82" textLength="778" lengthAdjust="spacingAndGlyphs">
        <tspan class="b c-red">HEALTHCARE</tspan><tspan class="b c-blue"> NEEDS</tspan></text>
      <text x="74" y="483" font-size="72" textLength="703" lengthAdjust="spacingAndGlyphs">
        <tspan class="l c-ink">OF </tspan><tspan class="b c-ink">OUR COMMUNITY</tspan><tspan class="l c-ink">.</tspan></text>
    </svg>
  </section>

  <svg class="banner" width="846" height="55" viewBox="0 0 846 55">
    <rect x="0" y="0" width="846" height="55" fill="var(--red)"/>
    <polygon points="0,0 440,0 425,55 0,55" fill="var(--blue)"/>
    <text x="30" y="40" font-size="31" font-weight="900" fill="var(--yellow)" textLength="235" lengthAdjust="spacingAndGlyphs">FAST DELIVERY</text>
    <text x="273" y="40" font-size="31" font-weight="700" fill="#fff" textLength="133" lengthAdjust="spacingAndGlyphs">SERVICE!</text>
    <text x="455" y="41" font-size="33" font-weight="700" fill="#fff" textLength="90" lengthAdjust="spacingAndGlyphs">CALL:</text>
    <text x="555" y="42" font-size="38" font-weight="900" fill="var(--yellow)" textLength="265" lengthAdjust="spacingAndGlyphs">650-555-0148</text>
  </svg>

  <section class="features">
    <div class="feature" style="left:116px">
      <svg viewBox="0 0 64 64" fill="none" stroke="var(--red)" stroke-width="3" stroke-linecap="round">
        <path d="M18 4 C18 24 46 40 46 60"/><path d="M46 4 C46 24 18 40 18 60"/>
        <path d="M20 12h24M25 20h14M25 44h14M20 52h24"/>
      </svg>
      <h3>EXTENDED<br>HOURS</h3>
      <p>Lorem ipsum dolor<br>sit amet, consectetur<br>adipiscing elit,</p>
    </div>
    <div class="feature" style="left:320px">
      <svg viewBox="0 0 64 64" fill="none" stroke="var(--red)" stroke-width="3" stroke-linecap="round">
        <path d="M14 6h-4v14c0 10 8 16 14 16s14-6 14-16V6h-4"/>
        <path d="M24 36v8c0 10 8 14 16 14s12-6 12-14v-4"/>
        <circle cx="52" cy="34" r="6"/><circle cx="52" cy="34" r="1.5" fill="var(--red)"/>
      </svg>
      <h3>PERSONAL<br>CARE</h3>
      <p>Lorem ipsum dolor<br>sit amet, consectetur<br>adipiscing elit,</p>
    </div>
    <div class="feature" style="left:538px">
      <svg viewBox="0 0 64 64" fill="none" stroke="var(--red)" stroke-width="3" stroke-linejoin="round">
        <path d="M4 4h56v44H26l-10 10V48H4z"/>
        <path d="M20 38V14h9a6 6 0 0 1 0 12h-9M28 26l14 14M44 26l-12 14"/>
      </svg>
      <h3>SUPERIOR<br>SERVICE</h3>
      <p>Lorem ipsum dolor<br>sit amet, consectetur<br>adipiscing elit,</p>
    </div>
    <div class="feature" style="left:733px">
      <svg viewBox="0 0 64 64" fill="none" stroke="var(--red)" stroke-width="3" stroke-linejoin="round">
        <path d="M4 6h44l10 10v30H34M4 6v40h18"/>
        <path d="M12 16h28M12 24h36M12 32h20"/>
        <circle cx="42" cy="44" r="8"/><path d="M36 50l-3 10 6-3 3 5 2-8M48 50l2 8"/>
      </svg>
      <h3>EXPERT<br>ADVICE</h3>
      <p>Lorem ipsum dolor<br>sit amet, consectetur<br>adipiscing elit,</p>
    </div>
  </section>

  <table class="hours">
    <thead><tr><th>DAY</th><th>TIME</th><th>STATUS</th></tr></thead>
    <tbody>
      <tr><td class="day">Monday</td><td class="time">10a.m - 12:00m.n</td><td class="status">OPEN</td></tr>
      <tr><td class="day">Tuesday</td><td class="time">10a.m - 12:00m.n</td><td class="status">OPEN</td></tr>
      <tr><td class="day">Wednesday</td><td class="time">10a.m - 12:00m.n</td><td class="status">OPEN</td></tr>
      <tr><td class="day">Thursday</td><td class="time">10a.m - 12:00m.n</td><td class="status">OPEN</td></tr>
      <tr><td class="day">Friday</td><td class="time">10a.m - 4p.m</td><td class="status">OPEN</td></tr>
      <tr><td class="day">Saturday</td><td class="time">Motzei Shabbos til midnight</td><td class="status">OPEN</td></tr>
      <tr><td class="day">Sunday</td><td class="time">10a.m - 7p.m</td><td class="status">OPEN</td></tr>
    </tbody>
    <tfoot><tr><td></td><td></td><td></td></tr></tfoot>
  </table>

  <footer class="footer">
    <div class="address">#34 LOREM IPSUM DOLOR, SIT CITY</div>
    <div class="email">KESSLERPHARMACY@MAIL.COM</div>
  </footer>
</div>
</body>
</html>
```